Kestrel Table Hour Podcast Episode Cover

I’m looking for a clean, professional, and eye-catching podcast episode cover template for my show, Kestrel Table Hour. Each week, I feature a new guest, so the design must allow me (or my team) to easily swap in a new guest’s photo without needing advanced design skills.

The template should be:

- Drag-and-drop friendly: simple for me to replace the guest’s headshot in Canva, Photoshop, or similar.
- On-brand with the Kestrel Table Hour podcast: professional yet approachable, foodservice industry-focused.
- Bold and attention-grabbing for podcast platforms and social media.

Readable text at small sizes, since covers are often viewed as thumbnails.

Design Elements to Include:

1. Podcast Title: “Kestrel Table Hour” (prominently displayed)
2. Subtitle/Space: Line for guest’s name, professional title, and company name
3. Photo Placeholder: Large, central area where I can easily drag and drop a guest photo
4. Brand Colors: attached
5. Clean, modern fonts (easy to read at thumbnail size)
6. Background graphics or patterns that give a sense of foodservice, leadership, or nationwide reach... but do not overpower the guest photo

Format Requirements:

- Editable source file (PSD, Canva template, or layered AI/INDD)
- JPG/PNG exports for immediate use
- Square format (3000x3000px) for podcast platforms

Style Inspiration:
Think modern podcast covers: bold fonts, clean lines, professional with a touch of energy.

Deliverables:

1. Final episode cover template (editable file)
2. Instructions or guidance on how to swap out guest photos

```html
<!DOCTYPE html>
<html lang="en">
<head>
<meta charset="utf-8">
<title>Kestrel Table Hour – Episode Cover</title>
<link href="https://fonts.googleapis.com/css2?family=Bebas+Neue&family=Montserrat:wght@700;800&display=swap" rel="stylesheet">
<style>
  :root {
    --navy-deep: #1c3660;
    --navy: #1e3b66;
    --blue-glow: #3a7fbf;
    --gold: #f5b315;
    --white: #ffffff;
    --photo-bright: #e4e4e2;
    --photo-light: #c9c8c6;
    --photo-mid: #9c9895;
    --photo-dark: #5b534d;
  }
  html, body {
    margin: 0;
    padding: 0;
    width: 1200px;
    height: 1200px;
    overflow: hidden;
    background: var(--navy);
  }
  .cover {
    position: relative;
    width: 1200px;
    height: 1200px;
    overflow: hidden;
    background:
      radial-gradient(ellipse 380px 520px at 0 760px, var(--blue-glow) 0%, rgba(58,127,191,0) 100%),
      linear-gradient(160deg, var(--navy-deep) 0%, var(--navy) 60%, #1d3a66 100%);
  }
  .guest-photo {
    position: absolute;
    inset: 0;
    width: 1200px;
    height: 1200px;
  }
  .guest-photo svg {
    display: block;
    width: 1200px;
    height: 1200px;
  }
  .frame {
    position: absolute;
    left: 52px;
    top: 52px;
    width: 1092px;
    height: 1113px;
    border: 2px solid var(--gold);
    border-bottom: none;
    pointer-events: none;
  }
  .footer-band {
    position: absolute;
    left: 0;
    bottom: 0;
    width: 1200px;
    height: 33px;
    background: var(--gold);
  }
  .show-title {
    position: absolute;
    left: 94px;
    top: 78px;
    margin: 0;
    font-family: "Bebas Neue", "Oswald", sans-serif;
    font-weight: 400;
    line-height: 0.86;
  }
  .show-title .line-top {
    display: block;
    color: var(--white);
    font-size: 196px;
    letter-spacing: 2px;
    padding-left: 45px;
  }
  .show-title .line-bottom {
    display: block;
    color: var(--gold);
    font-size: 162px;
    letter-spacing: 5px;
  }
  .guest-info {
    position: absolute;
    left: 94px;
    top: 448px;
    font-family: "Montserrat", sans-serif;
    font-weight: 800;
  }
  .guest-info .with {
    margin: 0;
    color: var(--white);
    font-size: 37px;
    line-height: 1;
  }
  .guest-info .guest-name {
    margin: 16px 0 0;
    color: var(--gold);
    font-size: 82px;
    line-height: 1;
    letter-spacing: -1px;
  }
  .guest-info .guest-role {
    margin: 24px 0 0;
    color: var(--white);
    font-weight: 700;
    font-size: 35px;
    line-height: 1;
  }
</style>
</head>
<body>
  <main class="cover">
    <div class="guest-photo" role="img" aria-label="Guest photo placeholder: smiling chef in a white toque and chef jacket giving a thumbs up in a bright kitchen, with a steel range hood above">
      <svg viewBox="0 0 1200 1200" aria-hidden="true">
        <defs>
          <linearGradient id="kitchenTone" gradientUnits="userSpaceOnUse" x1="380" y1="1180" x2="1180" y2="160">
            <stop offset="0" stop-color="var(--photo-bright)"/>
            <stop offset="0.35" stop-color="var(--photo-light)"/>
            <stop offset="0.65" stop-color="var(--photo-mid)"/>
            <stop offset="1" stop-color="var(--photo-dark)"/>
          </linearGradient>
        </defs>
        <path class="photo-arc" d="M354 1200 C 380 860, 700 330, 1200 280 L1200 1200 Z" fill="url(#kitchenTone)"/>
        <path class="photo-corner" d="M1108 230 C 1118 170, 1160 141, 1200 141 L1200 230 Z" fill="url(#kitchenTone)"/>
      </svg>
    </div>

    <div class="frame"></div>

    <h1 class="show-title">
      <span class="line-top">KESTREL</span>
      <span class="line-bottom">TABLE HOUR</span>
    </h1>

    <section class="guest-info">
      <p class="with">WITH</p>
      <p class="guest-name">Marisol</p>
      <p class="guest-role">Chef, Harbor Lane Kitchen</p>
    </section>

    <div class="footer-band"></div>
  </main>
</body>
</html>
```